Buchcover-Design für Ratgeber für Eltern
Zielgruppe
Ich bin promovierte Pädagogin. Das Buch, für das ein Cover benötigt wird (für ebook und Printversion) ist ein Ratgeber für Eltern, die plötzlich mit eine Schreikind nach der Geburt konfrontiert sind. Dafür wird schnelle Hilfe durch Tipps ebenso wie Hintergrundinformationen im Sinne eines Fachbuchs gegeben. Buchtitel: Die Elternbrücke, Autorin: Katrin Brandt, der Untertitel: Fachbuch rund um das Thema 'Schreikind'.
Aufgabenstellung
Das Cover soll Eltern, insbesondere Mütter ansprechen, schnell ins Auge fallen und das Herz ansprechen und auf das Wesentliche reduziert sein, womit die formschöne Aufteilung und passende Schriftart, -farbe sehr wichtig werden. Es gibt ein Covervorbild, das Buch 'Kieselsommer' von Thomas Kern Wallrabe. Die Hintergrundfarbe sollte ein schönes, eher dunkleres pink/himbeer sein. Statt des Welpen sollte ein Babygesicht abgebildet sein. Die Schriftart des Titels sollte etwas weniger verspielt sein.
Ich bräuchte die Datei für ein ebook und später auch für ein Taschenbuch und Hardcover. Dafür ist sind die Breiten für die Buchrücken noch nicht klar. Die entsprechende Datei müsste später nochmals angepasst werden - eventuell auch erst in zwei, drei Monaten - das sollte in dem Auftrag eingeschlossen sein. Später wird eventuell ein angepasste Design für ein Hörbuch nötig, hier wäre die Möglichkeit zu späteren Zusammenarbeit wünschenswert.

```html
<!DOCTYPE html>
<html lang="de">
<head>
<meta charset="utf-8">
<title>Die Elternbrücke – Katrin Brandt</title>
<link rel="stylesheet" href="https://fonts.googleapis.com/css2?family=Roboto:wght@300;400;500&display=swap">
<style>
  :root {
    --raspberry: #c70c44;
    --raspberry-light: #d8416a;
    --white: #ffffff;
    --rule: rgba(255, 255, 255, 0.85);
    --skin: #efd2bd;
    --vest: #3e2c25;
  }
  html, body {
    margin: 0;
    padding: 0;
    overflow: hidden;
    background: var(--raspberry);
  }
  .cover {
    position: relative;
    width: 817px;
    height: 1200px;
    background: var(--raspberry);
    color: var(--white);
    font-family: "Roboto", Arial, sans-serif;
    overflow: hidden;
  }
  .title {
    position: absolute;
    top: 100px;
    left: 0;
    width: 100%;
    margin: 0;
    text-align: center;
    font-weight: 300;
    line-height: 1;
  }
  .title-small {
    display: block;
    font-size: 58px;
  }
  .title-main {
    display: block;
    margin-top: 6px;
    font-size: 96px;
    letter-spacing: 0.5px;
  }
  .title-rule {
    position: absolute;
    top: 271px;
    left: 212px;
    width: 400px;
    height: 2px;
    background: var(--rule);
    border: 0;
    margin: 0;
  }
  .subtitle {
    position: absolute;
    top: 306px;
    left: 0;
    width: 100%;
    margin: 0;
    text-align: center;
    font-size: 25px;
    font-weight: 400;
  }
  .artwork {
    position: absolute;
    left: 0;
    top: 0;
  }
  .author {
    position: absolute;
    top: 1090px;
    left: 0;
    width: 100%;
    margin: 0;
    text-align: center;
    font-size: 23px;
    font-weight: 500;
    letter-spacing: 1.5px;
    text-transform: uppercase;
  }
</style>
</head>
<body>
  <main class="cover">
    <h1 class="title">
      <span class="title-small">Die</span>
      <span class="title-main">Elternbrücke</span>
    </h1>
    <hr class="title-rule">
    <p class="subtitle">Fachbuch zum Thema ‘Schreikind’</p>

    <svg class="artwork" width="817" height="1200" viewBox="0 0 817 1200">
      <defs>
        <radialGradient id="babyTones" cx="50%" cy="35%" r="65%">
          <stop offset="0%" stop-color="var(--skin)"/>
          <stop offset="55%" stop-color="#e9e6ee"/>
          <stop offset="100%" stop-color="var(--vest)" stop-opacity="0.55"/>
        </radialGradient>
      </defs>
      <g role="img" aria-label="Dezentes Blütenornament im Kreis hinter dem Baby">
        <circle cx="409" cy="713" r="290" fill="var(--raspberry-light)" opacity="0.35"/>
        <circle cx="409" cy="713" r="290" fill="none" stroke="var(--raspberry-light)" stroke-width="3"/>
      </g>
      <g role="img" aria-label="Foto eines lächelnden Babys im Pullunder, krabbelnd">
        <ellipse cx="409" cy="675" rx="315" ry="290" fill="url(#babyTones)"/>
      </g>
    </svg>

    <p class="author">Katrin Brandt</p>
  </main>
</body>
</html>
```